Marlow Haven

Yoga and Pilates
I teach privates and small groups

Simple clean design 2-4 pages.
(Bookings will be though contacting me, so need for booking capabilities)

```html
<!DOCTYPE html>
<html lang="en">
<head>
<meta charset="utf-8">
<title>Marlow Haven – Yoga and Pilates</title>
<link href="https://fonts.googleapis.com/css2?family=Allura&family=Poppins:wght@400;500;600;700&display=swap" rel="stylesheet">
<style>
:root{
  --red:#ec5a5c;
  --red-deep:#a5282c;
  --ink:#1c1c1c;
  --body:#4a4a4a;
  --muted:#9a9a9a;
  --light:#f2f2f2;
  --white:#ffffff;
  --line:#bdbdbd;
  --footer:#2e1414;
}
*{box-sizing:border-box;margin:0;padding:0}
html,body{width:1200px;height:3769px;overflow:hidden}
body{font-family:'Poppins',sans-serif;color:var(--body);background:var(--white);position:relative}
section,header,footer{position:relative;width:1200px;overflow:hidden}
.abs{position:absolute}
.script{font-family:'Allura',cursive;color:var(--red);font-size:44px;line-height:1}
.title{font-weight:700;color:var(--ink);font-size:38px;line-height:1.15}
.para{font-size:13px;line-height:23px;color:var(--body)}
.btn{position:absolute;background:var(--red);color:var(--white);font-weight:500;font-size:13.5px;text-transform:uppercase;display:flex;align-items:center;justify-content:center;letter-spacing:.2px}
.ph{position:absolute}

/* hero */
.hero{height:629px}
.hero-photo{left:0;top:0;width:1200px;height:629px;background:linear-gradient(100deg,#2b2320 0%,#3d3330 45%,#5a4a44 70%,#3e3532 100%)}
.hero-figure{left:430px;top:100px;width:620px;height:529px;background:linear-gradient(180deg,rgba(214,150,160,.35),rgba(40,110,100,.55));border-radius:260px 260px 40px 40px}
.brand{left:158px;top:16px;display:flex;align-items:center;gap:10px;color:var(--white);font-size:24px;font-weight:500}
.brand i{width:14px;height:14px;border-radius:50%;background:var(--red);display:block}
.nav{left:472px;top:24px;display:flex}
.nav a{color:var(--white);text-decoration:none;font-size:13px;width:98px;position:relative}
.nav a.on::after{content:"";position:absolute;left:12px;top:24px;width:10px;height:4px;border-radius:2px;background:var(--red)}
.call{left:868px;top:12px;width:175px;height:43px;background:var(--red);color:var(--white);font-size:14px;display:flex;align-items:center;justify-content:center;gap:10px}
.hero .script{left:158px;top:200px;color:var(--white);font-size:62px}
.hero h1{left:158px;top:266px;color:var(--white);font-size:52px;font-weight:700}
.hero p{left:160px;top:343px;color:var(--white);font-size:23px;font-weight:500}

/* appointment */
.booking{height:436px;background:var(--light)}
.cal{left:158px;top:37px;width:351px;height:365px;background:var(--red);padding:14px}
.cal-in{background:var(--white);width:100%;height:100%;padding:22px 0 0}
.cal-head{display:flex;justify-content:center;position:relative;font-size:15px;font-weight:500;color:var(--ink);letter-spacing:.5px}
.cal-head span{position:absolute;right:22px;top:0;font-size:14px}
.cal-grid{display:grid;grid-template-columns:repeat(7,1fr);padding:0 6px;margin-top:26px}
.cal-grid b{font-size:10.5px;font-weight:500;color:var(--ink);text-align:center;height:34px}
.cal-grid i{font-style:normal;font-size:13px;text-align:center;height:46px;line-height:32px;color:var(--ink)}
.cal-grid i.off{color:#c8c8c8}
.cal-grid i.today span{display:inline-block;width:34px;height:34px;line-height:32px;border:1.5px solid #3aa0e0;border-radius:50%}
.booking .script{left:593px;top:60px}
.booking .title{left:593px;top:102px}
.booking .para{left:593px;width:450px}

/* about */
.about{height:486px}
.about-frame{left:588px;top:56px;width:430px;height:349px;background:var(--red)}
.about-photo{left:612px;top:78px;width:430px;height:352px;background:linear-gradient(160deg,#d8d2cc,#a69a92 55%,#6c5e58)}
.play{left:797px;top:230px;width:60px;height:60px;border-radius:50%;background:var(--red);display:flex;align-items:center;justify-content:center}

/* classes */
.classes{height:604px;background:linear-gradient(120deg,#b33034,var(--red-deep) 60%,#9a2528)}
.center{left:0;width:1200px;text-align:center}
.classes > .script{color:var(--white);top:56px}
.classes > .title{color:var(--white);top:100px}
.cards{left:158px;top:165px;display:flex;gap:18px}
.card{width:282px;height:323px;background:var(--white);border-radius:0 26px 0 0;position:relative;overflow:hidden;text-align:center}
.card .ph{left:0;top:0;width:282px;height:193px}
.pill{position:absolute;left:40px;top:172px;width:234px;height:44px;border-radius:22px;background:var(--red);color:var(--white);font-size:12px;display:flex;align-items:center;justify-content:center;gap:10px}
.card .card-tag{position:absolute;left:0;right:0;top:226px;font-size:25px}
.card h3{position:absolute;left:0;right:0;top:256px;font-size:16.5px;font-weight:600;color:var(--ink)}
.card p{position:absolute;left:0;right:0;top:285px;font-size:13px;color:#666}

/* facilities */
.facilities{height:632px}
.facilities .script{top:40px}
.facilities .title{top:84px}
.halo{left:443px;top:158px;width:314px;height:314px;border-radius:50%;background:#f3f3f3}
.figure{left:480px;top:160px;width:260px;height:430px;background:linear-gradient(180deg,#e8cdbd,#2b3550 55%,#1f2a45);border-radius:130px 130px 60px 60px}
.ico{width:90px;height:90px;border-radius:50%;background:var(--red);display:flex;align-items:center;justify-content:center}
.ico::before{content:"";position:absolute;left:-4px;top:0;width:14px;height:14px;border-radius:50%;background:#f49b9c}
.feat h4{font-size:16.5px;font-weight:600;color:var(--ink);margin-bottom:12px}
.feat p{font-size:13px;line-height:23px}
.feat.l{text-align:right;width:230px}
.feat.r{width:230px}

/* contact */
.contact{height:478px;background:var(--light)}
.contact .script{left:155px;top:80px}
.contact .title{left:156px;top:122px;font-size:36px}
.info{left:158px;display:flex;gap:15px}
.info .sq{width:58px;height:58px;background:var(--red);display:flex;align-items:center;justify-content:center}
.info strong{display:block;font-weight:500;color:var(--ink);font-size:14.5px;margin-top:4px}
.info span{font-size:14px;color:#777;line-height:22px}
.field{position:absolute;border:1.5px solid #b9b9b9;background:var(--white);font-size:12px;color:#777;padding:13px 14px}

/* footer */
.footer{height:463px;background:linear-gradient(160deg,#3b1a1a,var(--footer) 50%,#1f0d0d)}
.footer h2{left:158px;top:88px;color:var(--white);font-size:28px;font-weight:700}
.footer h5{color:var(--white);font-size:15px;font-weight:500}
.footer h5::after{content:"";display:block;width:44px;height:3px;background:var(--red);margin-top:6px}
.hours{left:158px;top:148px;color:var(--white);font-size:14px}
.hours table{margin-top:12px;border-collapse:collapse}
.hours td{padding:0 0 12px;font-size:13px}
.hours td.d{color:var(--red);width:122px;font-size:12px}
.links{list-style:none;color:var(--white);font-size:13px}
.links li{height:29px}
.links li::before{content:"»";margin-right:24px}
.gallery{left:833px;top:159px;display:grid;grid-template-columns:repeat(3,66px);gap:7px}
.gallery div{height:48px;background:linear-gradient(135deg,#c77a70,#4f6f90)}
.gallery div:nth-child(3n+2){background:linear-gradient(135deg,#8fa6b8,#d8c4a8)}
.gallery div:nth-child(3n){background:linear-gradient(135deg,#e06060,#6a3a40)}
.touch{left:158px;top:325px;display:flex;align-items:center;gap:16px;color:var(--white);font-size:15px}
.touch .in{width:284px;height:43px;background:var(--white);color:#555;font-size:13px;display:flex;align-items:center;justify-content:space-between;padding:0 12px 0 18px}
.touch .go{width:30px;height:30px;border-radius:50%;background:var(--red);display:flex;align-items:center;justify-content:center}
.copy{left:0;width:1200px;top:395px;text-align:center;color:var(--white);font-size:12.5px}
.copy span{color:var(--red)}
.bar{height:41px;background:var(--red);display:flex;justify-content:center;align-items:center;gap:7px}
.bar i{width:28px;height:28px;border-radius:50%;background:var(--white);display:block}
</style>
</head>
<body>

<header class="hero">
  <div class="ph hero-photo" role="img" aria-label="Photo of a woman in teal activewear stretching in a low side lunge in front of a dark shutter"></div>
  <div class="ph hero-figure" role="img" aria-label="Yoga instructor stretching"></div>
  <div class="abs brand"><i></i>Marlow Haven</div>
  <nav class="abs nav"><a class="on">Home</a><a>About</a><a>Classes</a><a>Contact</a></nav>
  <div class="abs call">
    <svg width="22" height="22" viewBox="0 0 24 24"><circle cx="12" cy="12" r="10.5" fill="none" stroke="#fff" stroke-width="1.5"/><path d="M8.5 7c.6-.4 1.2-.3 1.5.2l1 1.7c.3.5.1 1-.3 1.3l-.6.4c.5 1.3 1.5 2.4 2.8 3l.5-.6c.3-.4.9-.5 1.3-.2l1.7 1c.5.3.6 1 .2 1.5-.8 1-2 1.4-3.2.9-2.5-1-4.5-3-5.5-5.6-.4-1.1-.1-2.2.6-2.6z" fill="#fff"/></svg>
    (555) 014-3820
  </div>
  <div class="abs script">Welcome To</div>
  <h1 class="abs">Marlow Haven</h1>
  <p class="abs">Yoga Group Set Out To Reduce Anxiety</p>
  <div class="btn" style="left:158px;top:405px;width:176px;height:44px">Join Us Now</div>
</header>

<section class="booking">
  <div class="abs cal">
    <div class="cal-in">
      <div class="cal-head">APRIL 2022<span>→</span></div>
      <div class="cal-grid">
        <b>MON</b><b>TUE</b><b>WED</b><b>THU</b><b>FRI</b><b>SAT</b><b>SUN</b>
        <i class="off">28</i><i class="off">29</i><i class="off">30</i><i class="off">31</i><i class="off">1</i><i class="off">2</i><i class="off">3</i>
        <i class="today"><span>4</span></i><i>5</i><i>6</i><i>7</i><i>8</i><i>9</i><i class="off">10</i>
        <i>11</i><i>12</i><i>13</i><i>14</i><i>15</i><i>16</i><i class="off">17</i>
        <i>18</i><i>19</i><i>20</i><i>21</i><i>22</i><i>23</i><i class="off">24</i>
        <i>25</i><i>26</i><i>27</i><i>28</i><i>29</i><i>30</i><i class="off">1</i>
      </div>
    </div>
  </div>
  <div class="abs script">Make Easy To</div>
  <h2 class="abs title">Book An Appointment</h2>
  <p class="abs para" style="top:164px">Not sure where to start? Let us help you out! Whether you've been stuck on the couch for the last ten years, or are looking to take your fitness to the next level, this is your program!</p>
  <p class="abs para" style="top:257px">Totam rem eaquiti sociosqu ad litora hendrerit in vulputate velit esse mol Mauris odio ilms it con nec a odio sequat auctor.</p>
  <div class="btn" style="left:594px;top:331px;width:203px;height:44px">Book An Appointment</div>
</section>

<section class="about">
  <div class="abs script" style="left:158px;top:86px">Learn More</div>
  <h2 class="abs title" style="left:160px;top:130px">About Marlow Haven</h2>
  <p class="abs para" style="left:158px;top:196px;width:420px">Not sure where to start? Let us help you out! Whether you've been stuck on the couch for the last ten years, or are looking to take your fitness to the next level, this is your program!</p>
  <p class="abs para" style="left:158px;top:289px;width:420px">Totam rem eaquiti sociosqu ad litora hendrerit in vulputate velit esse mol Mauris odio ilms it con nec a odio sequat auctor.</p>
  <div class="btn" style="left:158px;top:353px;width:176px;height:44px">Read More</div>
  <div class="ph about-frame"></div>
  <div class="ph about-photo" role="img" aria-label="Video still of an instructor adjusting two women in a forward fold in a bright studio"></div>
  <div class="ph play"><svg width="18" height="20" viewBox="0 0 18 20"><path d="M3 2l13 8-13 8z" fill="#fff"/></svg></div>
</section>

<section class="classes">
  <div class="abs center script">Physical, Mental, And Spiritual Practice</div>
  <h2 class="abs center title">Our Classes</h2>
  <div class="abs cards">
    <article class="card">
      <div class="ph" role="img" aria-label="Group class holding a warrior pose in a gym" style="background:linear-gradient(135deg,#3a4650,#6d7f8a 60%,#2e3a44)"></div>
      <div class="pill">▢ Mar 4 ,2022 &nbsp;|&nbsp; ◷ 16:00 - 20:00</div>
      <div class="script card-tag">Many Desktop</div>
      <h3>Publishing Packages</h3>
      <p>25 / Number Of Week</p>
    </article>
    <article class="card">
      <div class="ph" role="img" aria-label="Students bending sideways with arms raised on yoga mats" style="background:linear-gradient(135deg,#b89890,#e2a070 50%,#6a8a9a)"></div>
      <div class="pill">▢ Mar 4 ,2022 &nbsp;|&nbsp; ◷ 16:00 - 20:00</div>
      <div class="script card-tag">Many Desktop</div>
      <h3>Publishing Packages</h3>
      <p>25 / Number Of Week</p>
    </article>
    <article class="card">
      <div class="ph" role="img" aria-label="Seated meditation class with hands joined at the chest" style="background:linear-gradient(135deg,#8a7a6a,#cdbda5 55%,#6d5f52)"></div>
      <div class="pill">▢ Mar 4 ,2022 &nbsp;|&nbsp; ◷ 16:00 - 20:00</div>
      <div class="script card-tag">Many Desktop</div>
      <h3>Publishing Packages</h3>
      <p>25 / Number Of Week</p>
    </article>
  </div>
  <div class="btn" style="left:512px;top:507px;width:175px;height:44px">View All Classes</div>
</section>

<section class="facilities">
  <div class="abs center script">Best Fasilites</div>
  <h2 class="abs center title">Of Marlow Haven</h2>
  <div class="ph halo"></div>
  <div class="ph figure" role="img" aria-label="Woman meditating cross-legged in a navy top"></div>

  <div class="abs feat l" style="left:153px;top:170px"><h4>Ashtanga Yoga</h4><p>Not sure where to start? Let us help you out! Whether you've been stuck on the couch</p></div>
  <div class="abs feat l" style="left:153px;top:358px"><h4>Boosts your Memory</h4><p>Not sure where to start? Let us help you out! Whether you've been stuck on the couch</p></div>
  <div class="abs feat r" style="left:813px;top:170px"><h4>Ashtanga Yoga</h4><p>Not sure where to start? Let us help you out! Whether you've been stuck on the couch</p></div>
  <div class="abs feat r" style="left:813px;top:358px"><h4>Mediation Coaching</h4><p>Not sure where to start? Let us help you out! Whether you've been stuck on the couch</p></div>

  <div class="abs ico" style="left:408px;top:170px"><svg width="40" height="40" viewBox="0 0 40 40" fill="none" stroke="#fff" stroke-width="2"><path d="M14 36V22l-4-8M26 36V22l4-8M17 8v16M23 8v16M20 6v18"/></svg></div>
  <div class="abs ico" style="left:694px;top:170px"><svg width="40" height="40" viewBox="0 0 40 40" fill="none" stroke="#fff" stroke-width="2"><circle cx="20" cy="12" r="4"/><path d="M8 22h24M20 16v12M14 36l6-8 6 8"/></svg></div>
  <div class="abs ico" style="left:408px;top:358px"><svg width="40" height="40" viewBox="0 0 40 40" fill="none" stroke="#fff" stroke-width="2"><path d="M20 8c-6 0-11 4-11 10 0 4 2 6 4 8v6h14v-6c2-2 4-4 4-8 0-6-5-10-11-10zM20 8v24M14 16h4M22 22h4"/></svg></div>
  <div class="abs ico" style="left:694px;top:358px"><svg width="40" height="40" viewBox="0 0 40 40" fill="none" stroke="#fff" stroke-width="2"><path d="M20 10c3 3 3 9 0 13-3-4-3-10 0-13zM20 23c-4-1-8-4-9-9 4 0 8 3 9 9zM20 23c4-1 8-4 9-9-4 0-8 3-9 9zM8 26c4 4 20 4 24 0M12 32h16"/></svg></div>
</section>

<section class="contact">
  <div class="abs script">Would You Like</div>
  <h2 class="abs title">Discuss A Yoga?</h2>
  <div class="abs info" style="top:180px"><div class="sq"><svg width="20" height="16" viewBox="0 0 20 16"><rect x="1" y="1" width="18" height="14" fill="none" stroke="#fff" stroke-width="2"/><path d="M1 1l9 7 9-7" fill="none" stroke="#fff" stroke-width="2"/></svg></div><div><strong>Email</strong><span>hello@marlowhaven.example</span></div></div>
  <div class="abs info" style="top:253px"><div class="sq"><svg width="20" height="20" viewBox="0 0 24 24"><path d="M6 3c1-.6 2-.4 2.4.3l1.6 2.8c.4.8.2 1.6-.5 2.1l-1 .7c.8 2.1 2.4 3.9 4.5 4.8l.8-1c.5-.6 1.4-.8 2.1-.4l2.8 1.6c.8.5.9 1.6.3 2.4-1.2 1.6-3.2 2.2-5.1 1.4-4-1.6-7.2-4.8-8.8-9-.6-1.8 0-3.8.9-4.7z" fill="#fff"/></svg></div><div><strong>Phone</strong><span>0555-014-382</span></div></div>
  <div class="abs info" style="top:325px"><div class="sq"><svg width="18" height="22" viewBox="0 0 18 22"><path d="M9 1a7 7 0 0 1 7 7c0 5-7 13-7 13S2 13 2 8a7 7 0 0 1 7-7z" fill="#fff"/><circle cx="9" cy="8" r="2.5" fill="#ec5a5c"/></svg></div><div><strong>Location</strong><span>48 Linden Row Suite 12<br>Fairview</span></div></div>

  <div class="field" style="left:489px;top:104px;width:273px;height:43px">First Name</div>
  <div class="field" style="left:769px;top:104px;width:273px;height:43px">Last Name</div>
  <div class="field" style="left:489px;top:155px;width:273px;height:43px">Phone Number</div>
  <div class="field" style="left:769px;top:155px;width:273px;height:43px">Email Address</div>
  <div class="field" style="left:489px;top:208px;width:553px;height:118px">Message</div>
  <div class="btn" style="left:489px;top:334px;width:174px;height:44px">Send Message</div>
</section>

<footer class="footer">
  <h2 class="abs">Marlow Haven</h2>
  <div class="abs hours">Opening Hours
    <table>
      <tr><td class="d">MON - THUR :</td><td>5am to 9pm</td></tr>
      <tr><td class="d">FRIDAY :</td><td>5am to 7pm</td></tr>
      <tr><td class="d">SAT - SUN :</td><td>7am to 2pm</td></tr>
    </table>
  </div>
  <div class="abs" style="left:458px;top:92px"><h5>Quick Link</h5></div>
  <ul class="abs links" style="left:458px;top:154px"><li>Home</li><li>About</li><li>Classes</li><li>Contact</li></ul>
  <div class="abs" style="left:616px;top:92px"><h5>Classes</h5></div>
  <ul class="abs links" style="left:616px;top:154px"><li>Lorem Ipsum</li><li>Contrary to popular</li><li>Lorem Ipsum</li><li>Contrary to popular</li></ul>
  <div class="abs" style="left:833px;top:92px"><h5>Gallery</h5></div>
  <div class="abs gallery" role="img" aria-label="Grid of nine yoga class photos">
    <div></div><div></div><div></div><div></div><div></div><div></div><div></div><div></div><div></div>
  </div>
  <div class="abs touch">Get In Touch
    <div class="in">Enter Your mail Id<span class="go"><svg width="14" height="14" viewBox="0 0 14 14"><path d="M1 7l12-6-4 12-2-5z" fill="#fff"/></svg></span></div>
  </div>
  <div class="abs copy">© All right reserved 2022 <span>Marlowhaven</span></div>
</footer>

<div class="bar"><i></i><i></i><i></i></div>

</body>
</html>
```